Agricultural Consulting Website

Provide a modern yet business like website for my new Agriculture Consulting Business in Australia called FenTrove. Whilst we are based in Australia we are targetting both domestic and international markets (especially in Asia). We are targetting corporate, small business, government and farmer clients. The design should compliment our logo also sourced through pixel guild. The webiste should be easy for me to keep updated on a regular basis without the need to go back to the designer.

Industry/Entity Type

Business

Requirements
Must have
• clean crisp feel
• be modern yet business like
• be able to be updated by myself easily

```html
<!DOCTYPE html>
<html lang="en">
<head>
<meta charset="utf-8">
<title>FenTrove – Agricultural Consulting</title>
<link href="https://fonts.googleapis.com/css2?family=Open+Sans:ital,wght@0,400;0,600;0,700;1,400&family=Questrial&display=swap" rel="stylesheet">
<style>
:root{
  --green:#5b9a0d;
  --green-dark:#4c840a;
  --brown:#6b3608;
  --text:#1e1e1e;
  --muted:#555;
  --panel:#efefef;
  --line:#333;
  --social:#e2d8cc;
}
*{box-sizing:border-box;margin:0;padding:0}
html,body{width:942px;height:1200px;overflow:hidden;background:#fff}
body{position:relative;font-family:"Open Sans",sans-serif;color:var(--text);font-size:10px;line-height:1.25}
.abs{position:absolute}
.top-rule{left:0;top:0;width:942px;height:3px;background:var(--green)}
.field-backdrop{left:0;top:0;width:942px;height:470px;background:linear-gradient(180deg,#f4f5f2 0%,#e9ece6 12%,#c9d6bb 30%,#aac48c 55%,#c4d6ae 75%,#ffffff 100%)}
.brand{left:78px;top:20px;display:flex;align-items:center;gap:8px}
.brand-mark{width:52px;height:53px;background:var(--green)}
.brand-name{font-family:"Questrial",sans-serif;font-size:36px;color:var(--green);letter-spacing:-.5px}
.nav{left:442px;top:0;height:32px;display:flex;background:var(--green)}
.nav a{display:block;height:32px;line-height:31px;color:#fff;text-decoration:none;font-family:"Questrial",sans-serif;font-size:13px;font-weight:bold;text-align:center;border-right:1px solid #73ab2f}
.nav a.current{background:var(--brown);position:relative}
.nav a.current::after{content:"";position:absolute;left:0;top:32px;border-left:39px solid transparent;border-right:39px solid transparent;border-top:6px solid var(--brown)}
.hero{left:78px;top:92px;width:785px;height:296px;background:linear-gradient(180deg,#fbfbfb,#e4e4e4)}
.hero-edge{left:78px;top:386px;width:785px;height:6px}
.hero-phone{left:692px;top:92px;width:171px;height:31px;color:#fff;font-family:"Questrial",sans-serif;font-size:20px;font-weight:bold;display:flex;align-items:center;justify-content:flex-end;padding-right:14px;gap:6px;isolation:isolate}
.hero-phone::before{content:"";position:absolute;inset:0;background:var(--green);clip-path:polygon(0 0,100% 0,100% 100%,14px 100%);z-index:-1}
.hero-photo{left:115px;top:123px;width:362px;height:223px;background:radial-gradient(ellipse at 58% 55%,#9fbf62 0%,#c9d6a4 30%,#e6ebe3 55%,#a8c28d 100%)}
.hero-title{left:509px;top:147px;width:325px;font-family:"Questrial",sans-serif;font-size:17px;font-weight:bold;color:var(--brown);line-height:1.3}
.hero-points{left:506px;top:210px;width:310px;list-style:none}
.hero-points li{display:flex;gap:7px;font-size:11px;line-height:1.15;margin-bottom:12px}
.hero-points svg{flex:none;margin-top:1px}
.cta{left:506px;top:294px;width:142px;height:32px;background:var(--green);color:#fff;font-family:"Questrial",sans-serif;font-size:16px;font-weight:bold;display:flex;align-items:center;justify-content:center}
.hero-more{left:660px;top:303px;font-family:"Questrial",sans-serif;font-size:12px;color:var(--brown)}
.slide-arrow{top:222px;width:28px;height:28px;border-radius:50%;background:rgba(255,255,255,.8);border:1px solid #ddd}
.section-head{left:78px;width:520px;display:flex;align-items:center;gap:7px;font-family:"Questrial",sans-serif;font-size:18px;font-weight:normal}
.section-head::before{content:"";width:22px;height:1px;background:var(--line)}
.section-head::after{content:"";flex:1;height:1px;background:var(--line)}
.copy{left:78px;width:520px;font-size:9.8px;line-height:1.3}
.more-link{font-family:"Questrial",sans-serif;font-size:12px;color:var(--brown)}
.service{top:684px;width:125px;height:206px;border:1px solid #ddd;background:#fff}
.service h3{position:absolute;left:9px;top:13px;font-family:"Questrial",sans-serif;font-size:12px;font-weight:bold;color:var(--brown)}
.service.lead h3{color:var(--green)}
.service-photo{position:absolute;left:7px;top:37px;width:111px;height:76px}
.service p{position:absolute;left:6px;top:123px;width:115px;font-size:8.8px;line-height:1.2}
.service .service-more{position:absolute;left:6px;top:175px;font-size:9.5px;font-weight:bold;color:var(--brown)}
.service.lead .service-more{color:var(--green)}
.service-bar{position:absolute;left:-1px;bottom:-1px;width:72px;height:5px;background:var(--brown);clip-path:polygon(0 0,94% 0,100% 100%,0 100%)}
.service.lead .service-bar{background:var(--green)}
.sidebar{left:638px;top:423px;width:226px;height:466px;background:var(--panel);border:1px solid #ddd}
.sidebar-title{left:656px;top:445px;font-family:"Questrial",sans-serif;font-size:16px}
.sidebar-rule{left:656px;top:477px;width:195px;height:1px;background:var(--line)}
.news{left:656px;width:200px;display:flex;gap:6px;font-size:9.5px;line-height:1.25}
.news p{width:150px}
.news-date{flex:none;width:34px;height:34px;border-radius:50%;background:var(--green);color:#fff;text-align:center;font-family:"Questrial",sans-serif;font-size:13px;line-height:1;padding-top:6px}
.news-date small{display:block;font-size:7px}
.news em{font-style:normal;color:var(--brown)}
.social-box{left:651px;top:656px;width:202px;height:220px;background:#fff;border:1px solid #ccc}
.social-head{left:660px;top:667px;width:185px;height:24px;background:var(--brown);color:#fff;font-family:"Questrial",sans-serif;font-weight:bold;font-size:12px;display:flex;align-items:center;padding-left:24px}
.social-name{left:659px;top:701px;display:flex;gap:10px;align-items:flex-start}
.social-name .sq{width:34px;height:34px;background:var(--green)}
.social-name b{color:#3b5998;font-size:10px;display:block}
.social-name span{display:inline-block;margin-top:3px;border:1px solid #ccc;background:#eef;font-size:7px;padding:1px 4px;color:#3b5998}
.social-div{left:652px;top:745px;width:200px;height:1px;background:#ddd}
.social-count{left:664px;top:753px;font-size:7.5px}
.social-count a{color:#3b5998;text-decoration:none}
.fans{left:664px;top:770px;width:178px;height:72px;display:grid;grid-template-columns:repeat(5,33px);grid-gap:4px}
.fans div{background:linear-gradient(135deg,#8a8f96,#d7d2c7)}
.social-foot{left:662px;top:859px;font-size:7.5px;display:flex;align-items:center;gap:5px}
.social-foot i{width:8px;height:8px;background:#3b5998;display:block}
.phone-band-line{left:316px;top:956px;width:344px;height:1px;background:var(--green)}
.phone-band-tag{left:372px;top:937px;width:226px;height:40px;color:#fff;font-family:"Questrial",sans-serif;font-size:23px;font-weight:bold;display:flex;align-items:center;justify-content:center;gap:8px;isolation:isolate}
.phone-band-tag::before{content:"";position:absolute;inset:0;background:var(--green);clip-path:polygon(0 0,100% 0,97% 50%,100% 100%,0 100%,3% 50%);z-index:-1}
.foot-col h4{font-family:"Open Sans",sans-serif;font-size:11.5px;font-weight:bold;color:var(--brown);margin-bottom:14px}
.foot-col ul{list-style:none}
.foot-col li{font-size:9.8px;color:var(--muted);margin-bottom:8.5px;padding-left:9px;position:relative}
.foot-col li::before{content:"";position:absolute;left:0;top:4px;width:4px;height:4px;background:#666}
.quote{font-size:9.8px;color:var(--muted);line-height:1.15;width:170px}
.quote-by{font-style:italic;color:var(--green);font-size:10.5px;margin:6px 0 16px}
.social-dots{display:flex;gap:10px}
.social-dots div{width:34px;height:34px;border-radius:50%;background:var(--social)}
.copyright{font-size:10.5px;font-weight:bold;margin-top:14px;padding-left:4px}
</style>
</head>
<body>
<div class="abs top-rule"></div>
<div class="abs field-backdrop" role="img" aria-label="Soft-focus green crop field under a pale sky"></div>

<div class="abs brand"><div class="brand-mark"></div><span class="brand-name">FenTrove</span></div>

<nav class="abs nav">
  <a href="#" style="width:66px">Home</a>
  <a href="#" class="current" style="width:78px">About us</a>
  <a href="#" style="width:76px">Services</a>
  <a href="#" style="width:75px">Contact</a>
  <a href="#" style="width:62px">FAQ's</a>
  <a href="#" style="width:63px;border-right:0">Blog</a>
</nav>

<div class="abs hero"></div>
<svg class="abs hero-edge" width="785" height="6" viewBox="0 0 785 6"><pattern id="zz" width="6" height="6" patternUnits="userSpaceOnUse"><path d="M0 0H6V1L3 5L0 1Z" fill="#cfcfcf"/></pattern><rect width="785" height="6" fill="url(#zz)"/></svg>
<div class="abs hero-phone"><svg width="13" height="15" viewBox="0 0 24 24"><path fill="#fff" d="M6.6 10.8a15 15 0 0 0 6.6 6.6l2.2-2.2a1 1 0 0 1 1-.3 11 11 0 0 0 3.6.6 1 1 0 0 1 1 1V20a1 1 0 0 1-1 1A17 17 0 0 1 3 4a1 1 0 0 1 1-1h3.5a1 1 0 0 1 1 1c0 1.3.2 2.5.6 3.6a1 1 0 0 1-.3 1z"/></svg>1800 555 014</div>
<div class="abs hero-photo" role="img" aria-label="Consultant in a white shirt holding a young green plant in cupped hands, field behind"></div>
<h1 class="abs hero-title">Lorem ipsum dolor sit amet, conse ctetur ad ipiscing elit. In fermentum dolor</h1>
<ul class="abs hero-points">
  <li><svg width="16" height="16" viewBox="0 0 16 16"><circle cx="8" cy="8" r="7.5" fill="#111"/><circle cx="8" cy="8" r="5.5" fill="none" stroke="#fff" stroke-width=".8"/><path d="M5 8.2l2 2 4-4.4" fill="none" stroke="#fff" stroke-width="1.4"/></svg>Lorem ipsum dolor sit amet, adipising consectetur dolor sit amet dolor sit amet adipising</li>
  <li><svg width="16" height="16" viewBox="0 0 16 16"><circle cx="8" cy="8" r="7.5" fill="#111"/><circle cx="8" cy="8" r="5.5" fill="none" stroke="#fff" stroke-width=".8"/><path d="M5 8.2l2 2 4-4.4" fill="none" stroke="#fff" stroke-width="1.4"/></svg>Lorem ipsum dolor sit amet, adipising consectetur dolor sit amet dolor sit amet adipising</li>
</ul>
<div class="abs cta">Call to Action</div>
<div class="abs hero-more">Learn More &gt;&gt;</div>
<svg class="abs slide-arrow" style="left:42px" viewBox="0 0 28 28"><path d="M16 9l-5 5 5 5" fill="none" stroke="#999" stroke-width="2.5"/></svg>
<svg class="abs slide-arrow" style="left:872px" viewBox="0 0 28 28"><path d="M12 9l5 5-5 5" fill="none" stroke="#999" stroke-width="2.5"/></svg>

<h2 class="abs section-head" style="top:452px">About Us</h2>
<p class="abs copy" style="top:481px">Lorem ipsum dolor sit amet, consectetur adipiscing elit. In fermentum dolor non augue pretium egestas. Donec sem eros, tincidunt at congue ut, posuere sit amet est. Vivamus scelerisque viverra odio sit amet laoreet. Ut nec neque non justo rutrum tempor lobortis eu ante. Aliquam sagittis, nibh quis commodo auctor, risus mauris laoreet lectus, id facilisis libero odio nec enim. Sed id ligula adipiscing purus lacinia aliquet. Ut nec neque non justo rutrum tempor lobortis eu ante. Aliquam sagittis, nibh quis commodo auctor, risus mauris laoreet lectus, id facilisis libero odio nec enim. Sed id ligula adipiscing purus lacinia aliquet.</p>
<div class="abs more-link" style="left:526px;top:577px">Learn More &gt;&gt;</div>

<h2 class="abs section-head" style="top:607px">Our Services</h2>
<p class="abs copy" style="top:636px">Lorem ipsum dolor sit amet, consectetur adipiscing elit. In fermentum dolor non augue pretium egestas. Donec sem eros, tincidunt at congue ut, posuere sit amet est. Vivamus scelerisque viverra odio sit amet laoreet.</p>

<div class="abs service lead" style="left:78px"><h3>Lorem Ipsum Text</h3><div class="service-photo" role="img" aria-label="Farmer standing beside hay bales in a harvested field" style="background:linear-gradient(180deg,#b8c6d4,#c9a865 55%,#8e7443)"></div><p>Lorem ipsum dolor sit amet, consec tetur adipis cing elit.In ferme ntum dolor non augue</p><span class="service-more">Learn More &gt;&gt;</span><div class="service-bar"></div></div>
<div class="abs service" style="left:210px"><h3>Lorem Ipsum Text</h3><div class="service-photo" role="img" aria-label="Hands holding soil with a green seedling" style="background:radial-gradient(ellipse at 50% 60%,#c9a48a,#9ec06a 60%,#7ea446)"></div><p>Lorem ipsum dolor sit amet, consec tetur adipis cing elit.In ferme ntum dolor non augue</p><span class="service-more">Learn More &gt;&gt;</span><div class="service-bar"></div></div>
<div class="abs service" style="left:342px"><h3>Lorem Ipsum Text</h3><div class="service-photo" role="img" aria-label="Two advisers inspecting wheat stalks in a field" style="background:linear-gradient(180deg,#c7d6e4,#9bb27e 55%,#6f8c3e)"></div><p>Lorem ipsum dolor sit amet, consec tetur adipis cing elit.In ferme ntum dolor non augue</p><span class="service-more">Learn More &gt;&gt;</span><div class="service-bar"></div></div>
<div class="abs service" style="left:474px"><h3>Lorem Ipsum Text</h3><div class="service-photo" role="img" aria-label="Farmer kneeling to check crops under a cloudy sky" style="background:linear-gradient(180deg,#9ea3a6,#87a05a 50%,#5f7f2c)"></div><p>Lorem ipsum dolor sit amet, consec tetur adipis cing elit.In ferme ntum dolor non augue</p><span class="service-more">Learn More &gt;&gt;</span><div class="service-bar"></div></div>

<aside>
<div class="abs sidebar"></div>
<div class="abs sidebar-title">Latest News</div>
<div class="abs sidebar-rule"></div>
<div class="abs news" style="top:493px"><div class="news-date">22<small>NOV</small></div><p>Lorem ipsum dolor sit amet. In dolor non augue pretium egestas pretium &nbsp;<em>more &gt;&gt;&gt;</em></p></div>
<div class="abs news" style="top:541px"><div class="news-date">22<small>NOV</small></div><p>Lorem ipsum dolor sit amet,. In fermen tum sit dolor augue pretium <em>more &gt;&gt;&gt;</em></p></div>
<div class="abs news" style="top:590px"><div class="news-date">22<small>NOV</small></div><p>Lorem ipsum dolor sit amet. In dolor non augue pretium egestas pretium &nbsp;<em>more &gt;&gt;&gt;</em></p></div>

<div class="abs social-box"></div>
<div class="abs social-head">Find us on Friendwall</div>
<div class="abs social-name"><div class="sq"></div><div><b>FenTrove</b><span>Like</span></div></div>
<div class="abs social-div"></div>
<div class="abs social-count">5458 people like <a href="#">fentrove.com</a></div>
<div class="abs fans" role="img" aria-label="Grid of follower profile thumbnails"><div></div><div></div><div></div><div></div><div></div><div></div><div></div><div></div><div></div><div></div></div>
<div class="abs social-div" style="top:851px"></div>
<div class="abs social-foot"><i></i>Friendwall social Plugin</div>
</aside>

<div class="abs phone-band-line"></div>
<div class="abs phone-band-tag"><svg width="16" height="18" viewBox="0 0 24 24"><path fill="#fff" d="M6.6 10.8a15 15 0 0 0 6.6 6.6l2.2-2.2a1 1 0 0 1 1-.3 11 11 0 0 0 3.6.6 1 1 0 0 1 1 1V20a1 1 0 0 1-1 1A17 17 0 0 1 3 4a1 1 0 0 1 1-1h3.5a1 1 0 0 1 1 1c0 1.3.2 2.5.6 3.6a1 1 0 0 1-.3 1z"/></svg>1800 555 014</div>

<footer>
<div class="abs foot-col" style="left:77px;top:1013px"><h4>Information</h4><ul><li>Home</li><li>Log in</li><li>My Hood</li><li>Sell</li><li>Top Searches</li></ul></div>
<div class="abs foot-col" style="left:206px;top:1013px"><h4>Our Sevices</h4><ul><li>Lorem Ipsum Text</li><li>Lorem Ipsum Text</li><li>Lorem Ipsum Text</li><li>Lorem Ipsum Text</li></ul></div>
<div class="abs foot-col" style="left:356px;top:1013px"><h4>Testimonials</h4>
  <p class="quote">"Lorem ipsum dolor sit amet, consec tetur adipis cing elit.In ferme ntum dolor non augue "</p><p class="quote-by">Peter &nbsp;- &nbsp;Location</p>
  <p class="quote">"Lorem ipsum dolor sit amet, consec tetur adipis cing elit.In ferme ntum dolor non augue "</p><p class="quote-by">Peter &nbsp;- &nbsp;Location</p></div>
<div class="abs foot-col" style="left:582px;top:1013px"><h4>Legal</h4><ul><li>Privacy Policy</li><li>Terms and Condition</li><li>Presss</li></ul></div>
<div class="abs foot-col" style="left:738px;top:1013px"><h4>Social Icons</h4><div class="social-dots"><div></div><div></div><div></div></div><p class="copyright">© 2013</p></div>
</footer>
</body>
</html>
```